Business Card Design needed for logo design project

This project is linked to Crisp Lane Glow logo refresh..

Our company needs a Business Card Design. Please refer to our original project in the link above.

```html
<!DOCTYPE html>
<html lang="en">
<head>
<meta charset="utf-8">
<title>Crisp Lane Glow – Business Cards</title>
<link rel="stylesheet" href="https://fonts.googleapis.com/css2?family=Arimo:wght@400;700&family=Bubblegum+Sans&display=swap">
<style>
  :root{
    --bg:#1c1c1c;
    --card:#ffffff;
    --ink:#111111;
    --yellow:#f5e800;
    --red:#e2332a;
    --blue:#2aa3e0;
    --icon:#4a9fd6;
  }
  *{box-sizing:border-box;margin:0;padding:0}
  html,body{width:1200px;height:1000px;overflow:hidden}
  body{background:var(--bg);font-family:"Arimo",Arial,sans-serif;color:var(--ink);position:relative}
  .card{position:absolute;width:700px;height:400px;background:var(--card);overflow:hidden;box-shadow:0 6px 18px rgba(0,0,0,.5)}

  /* back card */
  .card--back{left:440px;top:60px}
  .stripes{position:absolute;display:flex;flex-direction:column;gap:4px}
  .stripes span{display:block;height:7px}
  .stripes .s-yellow{background:var(--yellow)}
  .stripes .s-red{background:var(--red)}
  .stripes .s-blue{background:var(--blue)}
  .stripes--left{left:0;top:105px;width:180px}
  .stripes--right{right:0;top:295px;width:180px}
  .brand{display:flex;align-items:center;gap:12px;font-weight:700;color:var(--red);white-space:nowrap;line-height:1}
  .card--back .brand{position:absolute;left:50%;top:155px;transform:translateX(-50%);font-size:44px}
  .brand__dot{width:20px;height:20px;border-radius:50%;background:var(--blue);flex:none}
  .back-url{position:absolute;left:0;right:0;top:238px;text-align:center;font-weight:700;font-size:24px;letter-spacing:.5px;line-height:1}

  /* front card */
  .card--front{left:60px;top:540px}
  .card--front .brand{position:absolute;left:34px;top:120px;font-size:38px}
  .claim{position:absolute;left:34px;top:236px;font-size:24px;line-height:1.1;text-transform:uppercase}
  .rule{position:absolute;left:0;right:0;top:308px;height:8px;background:var(--ink)}
  .band{position:absolute;left:0;right:0;top:316px;bottom:0;background:var(--yellow)}
  .region{position:absolute;left:34px;top:322px;font-size:14px;font-weight:700;text-transform:uppercase}
  .person{position:absolute;right:34px;top:22px;text-align:right;font-family:"Bubblegum Sans",cursive;line-height:1.1}
  .person__name{font-size:30px;color:var(--blue);letter-spacing:1px}
  .person__role{font-size:22px;color:var(--red)}
  .contacts{position:absolute;right:34px;top:100px;list-style:none;text-align:right;font-size:16px;line-height:1.2}
  .contacts li{display:flex;justify-content:flex-end;align-items:center;gap:10px;margin-bottom:4px}
  .contacts svg{width:20px;height:20px;flex:none}
  .contacts .addr{align-items:flex-end}
</style>
</head>
<body>

<section class="card card--back" aria-label="Business card back">
  <div class="stripes stripes--left"><span class="s-yellow"></span><span class="s-red"></span><span class="s-blue"></span></div>
  <div class="stripes stripes--right"><span class="s-yellow"></span><span class="s-red"></span><span class="s-blue"></span></div>
  <div class="brand"><span>Crisp Lane Glow</span><span class="brand__dot"></span></div>
  <p class="back-url">www.crisplaneglow.com</p>
</section>

<section class="card card--front" aria-label="Business card front">
  <div class="brand"><span>Crisp Lane Glow</span><span class="brand__dot"></span></div>
  <p class="claim">The Complate<br>Car Wash Company</p>
  <div class="rule"></div>
  <div class="band"></div>
  <p class="region">Serving Texas &amp; Oklahoma</p>

  <div class="person">
    <p class="person__name">Dale Merritt</p>
    <p class="person__role">President</p>
  </div>

  <ul class="contacts">
    <li>555-201-4837
      <svg viewBox="0 0 20 20"><rect width="20" height="20" rx="3" fill="var(--icon)"/><path d="M6 4c1 0 2 2 2 3s-1 1-1 2 2 3 3 3 1-1 2-1 3 1 3 2-1 2-2 2C8 15 5 12 5 6c0-1 0-2 1-2z" fill="#fff"/></svg></li>
    <li>555-201-4838
      <svg viewBox="0 0 20 20"><rect width="20" height="20" rx="3" fill="var(--icon)"/><rect x="4" y="8" width="12" height="8" fill="#fff"/><rect x="6" y="4" width="8" height="5" fill="#fff"/></svg></li>
    <li>555-309-6612
      <svg viewBox="0 0 20 20"><rect width="20" height="20" rx="3" fill="var(--icon)"/><rect x="6" y="3" width="8" height="14" rx="1.5" fill="#fff"/><rect x="7.5" y="5" width="5" height="5" fill="var(--icon)"/></svg></li>
    <li>dale@crisplaneglow.com
      <svg viewBox="0 0 20 20"><rect width="20" height="20" rx="3" fill="var(--icon)"/><rect x="3" y="5" width="14" height="10" fill="#fff"/><path d="M3 5l7 6 7-6" fill="none" stroke="var(--icon)" stroke-width="1.5"/></svg></li>
    <li class="addr"><span>1187 N. Alder Road, Irving<br>Texas 75099</span>
      <svg viewBox="0 0 20 20"><path d="M10 1a6 6 0 0 1 6 6c0 5-6 12-6 12S4 12 4 7a6 6 0 0 1 6-6z" fill="var(--icon)"/><circle cx="10" cy="7" r="2.3" fill="#fff"/></svg></li>
    <li>www.crisplaneglow.com
      <svg viewBox="0 0 20 20"><circle cx="10" cy="10" r="9" fill="var(--icon)"/><g fill="none" stroke="#fff" stroke-width="1.2"><circle cx="10" cy="10" r="7"/><ellipse cx="10" cy="10" rx="3" ry="7"/><path d="M3 10h14M4.5 6h11M4.5 14h11"/></g></svg></li>
  </ul>
</section>

</body>
</html>
```